Upscale Wine Cooler/Ready to drink Can Design

We need to design the branding and packaging for a new wine cooler that will be sold in a can. We are also looking for the brand name at this point, so you can be as creative as you can!

The product will have 3 flavours (Tressin Spritz, Ginger-Lime Spritz, Raspeberry-Mimosa) and will be made of genuine high quality European Wine, with natural flavours

Can dimensions : Height 157 mm ; Diameter : 58 mm
Updates

Need extra days to review

Target Market(s)

Females 19 to 35, who are looking for an alternative to the traditional alcoholic beverages, and who want to drink an upscale and "classy" beverage

Colors

Designer to choose colors to be used in the design.

Requirements
Must have
• Modern, attractive and upscale look
• Brand name
• 3 different cans for each of the flavours : Tressin Spritz, Ginger-Lime Spritz, Raspeberry-Mimosa
• 355 ml
• 5% alc./vol.

```html
<!DOCTYPE html>
<html lang="en">
<head>
<meta charset="utf-8">
<title>Velle – Wine Cooler Can Labels</title>
<link href="https://fonts.googleapis.com/css2?family=Lato:wght@300;400;700&display=swap" rel="stylesheet">
<style>
  :root {
    --page-bg: #e4e4e4;
    --ink: #121212;
    --band: #0d0d0f;
    --rose-light: #f3cfc3;
    --rose-mid: #e2a595;
    --rose-deep: #d38a78;
    --gold-light: #fbf1c8;
    --gold-mid: #efd88e;
    --gold-deep: #d9b560;
    --silver-light: #ffffff;
    --silver-mid: #e6e6e8;
    --silver-deep: #bfc0c4;
  }
  * { margin: 0; padding: 0; box-sizing: border-box; }
  html, body {
    width: 1200px;
    height: 749px;
    overflow: hidden;
    background: var(--page-bg);
    font-family: "Lato", Arial, sans-serif;
    color: var(--ink);
  }
  .label-row {
    position: relative;
    width: 1200px;
    height: 749px;
    display: flex;
    justify-content: center;
    align-items: center;
    gap: 36px;
  }
  .can-label {
    position: relative;
    width: 350px;
    height: 520px;
    display: flex;
    flex-direction: column;
    box-shadow: 0 6px 18px rgba(0,0,0,0.18);
  }
  .can-label__face {
    position: relative;
    flex: 1;
  }
  .can-label--rose .can-label__face {
    background: linear-gradient(135deg, var(--rose-light) 0%, var(--rose-mid) 30%, var(--rose-light) 52%, var(--rose-deep) 78%, var(--rose-light) 100%);
  }
  .can-label--gold .can-label__face {
    background: linear-gradient(135deg, var(--gold-mid) 0%, var(--gold-light) 30%, var(--gold-mid) 55%, var(--gold-deep) 80%, var(--gold-light) 100%);
  }
  .can-label--silver .can-label__face {
    background: linear-gradient(135deg, var(--silver-mid) 0%, var(--silver-light) 30%, var(--silver-deep) 58%, var(--silver-light) 82%, var(--silver-mid) 100%);
  }
  .can-label__band {
    height: 26px;
    background: linear-gradient(90deg, var(--band) 0%, #3a3b3f 50%, var(--band) 100%);
  }
  .brand-name {
    position: absolute;
    left: 0;
    right: 0;
    top: 92px;
    text-align: center;
    font-weight: 700;
    font-size: 42px;
    letter-spacing: 1px;
    line-height: 1;
  }
  .flavour {
    position: absolute;
    left: 0;
    right: 0;
    top: 190px;
    text-align: center;
  }
  .flavour__rule {
    width: 84px;
    height: 1px;
    margin: 0 auto;
    background: var(--ink);
  }
  .flavour__name {
    font-weight: 400;
    font-size: 15px;
    letter-spacing: 0.3px;
    padding: 14px 0;
  }
  .emblem-area {
    position: absolute;
    left: 105px;
    top: 300px;
    width: 140px;
    height: 80px;
    background: radial-gradient(ellipse at center, rgba(18,18,18,0.55) 0%, rgba(18,18,18,0.15) 60%, rgba(18,18,18,0) 75%);
  }
  .can-facts {
    position: absolute;
    left: 0;
    right: 0;
    bottom: 30px;
    display: flex;
    justify-content: space-between;
    padding: 0 78px 0 88px;
    font-size: 11px;
  }
</style>
</head>
<body>
<main class="label-row">

  <section class="can-label can-label--rose">
    <div class="can-label__face">
      <div class="brand-name">Velle</div>
      <div class="flavour">
        <div class="flavour__rule"></div>
        <div class="flavour__name">RASPEBERRY-MIMOSA</div>
        <div class="flavour__rule"></div>
      </div>
      <div class="emblem-area" role="img" aria-label="Brand emblem"></div>
      <div class="can-facts"><span>355 ml</span><span>5% alc./vol</span></div>
    </div>
    <div class="can-label__band"></div>
  </section>

  <section class="can-label can-label--gold">
    <div class="can-label__face">
      <div class="brand-name">Velle</div>
      <div class="flavour">
        <div class="flavour__rule"></div>
        <div class="flavour__name">TRESSIN SPRITZ</div>
        <div class="flavour__rule"></div>
      </div>
      <div class="emblem-area" role="img" aria-label="Brand emblem"></div>
      <div class="can-facts"><span>355 ml</span><span>5% alc./vol</span></div>
    </div>
    <div class="can-label__band"></div>
  </section>

  <section class="can-label can-label--silver">
    <div class="can-label__face">
      <div class="brand-name">Velle</div>
      <div class="flavour">
        <div class="flavour__rule"></div>
        <div class="flavour__name">GINGER-LIME SPRITZ</div>
        <div class="flavour__rule"></div>
      </div>
      <div class="emblem-area" role="img" aria-label="Brand emblem"></div>
      <div class="can-facts"><span>355 ml</span><span>5% alc./vol</span></div>
    </div>
    <div class="can-label__band"></div>
  </section>

</main>
</body>
</html>
```